Redesign and move to Wordpress for qorvanta.com

Our website needs a redesign and at the same time we are moving it to Wordpress. Please help us with a new digital professional look and feel.

We are an Australian Software Engineering company specialising in advanced software development using in A.I., PLatform Engineering, Integration and Cloud. See the current qorvanta.com for more information about us.

```html
<!DOCTYPE html>
<html lang="en">
<head>
<meta charset="utf-8">
<title>Qorvanta — AI-Powered Software Solutions</title>
<link rel="stylesheet" href="https://fonts.googleapis.com/css2?family=Exo+2:wght@400;500;600;700&family=Outfit:wght@300;400;500&display=swap">
<style>
:root{
  --navy:#0a1a44;
  --navy-deep:#081536;
  --teal:#4fc3b8;
  --teal-soft:#5cc7bd;
  --blue:#1a5dab;
  --blue-line:#7fb0e6;
  --ink:#1b1f2a;
  --grey:#555b66;
  --sub-bg:#123f4e;
  --white:#ffffff;
}
*{margin:0;padding:0;box-sizing:border-box}
html,body{width:1200px;height:3677px;overflow:hidden}
body{position:relative;font-family:"Outfit",sans-serif;color:var(--ink);background:var(--white)}
.abs{position:absolute}
.display{font-family:"Exo 2",sans-serif;text-transform:uppercase;letter-spacing:.5px}

/* header + hero */
.hero{left:0;top:0;width:1200px;height:620px;background:radial-gradient(ellipse at 75% 55%,#123a7a 0%,var(--navy) 45%,var(--navy-deep) 100%)}
.brand{display:flex;align-items:center;gap:14px;color:var(--white);font-family:"Exo 2",sans-serif;font-weight:400;font-size:30px;letter-spacing:1px}
.brand-square{width:34px;height:34px;border:2px solid var(--white)}
.main-nav{left:482px;top:36px;display:flex;gap:34px}
.main-nav a{color:var(--white);text-decoration:none;font-size:12.5px;font-weight:500;letter-spacing:.5px;font-family:"Exo 2",sans-serif}
.main-nav a.active{color:var(--teal);border-bottom:2px solid var(--teal);padding-bottom:8px}
.phone{left:908px;top:33px;display:flex;align-items:center;gap:12px;color:var(--white);font-family:"Exo 2",sans-serif;font-size:17px}
.hero-title{left:146px;top:152px;color:var(--white);font-weight:600;font-size:38px;line-height:50px}
.hero-title .accent{color:var(--teal);font-size:44px}
.hero-sub{left:148px;top:330px;color:#dfe6f3;font-size:18.5px;line-height:30px;font-weight:300}
.btn{display:inline-flex;align-items:center;justify-content:center;background:var(--teal);color:var(--navy);font-family:"Exo 2",sans-serif;font-weight:600;text-transform:uppercase;text-decoration:none}
.hero-btn{left:150px;top:420px;width:267px;height:49px;font-size:16px}
.dots{left:156px;top:547px;display:flex;gap:13px}
.dots span{width:13px;height:13px;border-radius:50%;border:1.5px solid var(--teal)}
.dots span.on{background:var(--teal)}
.hero-art{left:585px;top:107px;width:521px;height:464px;border-radius:50%;background:radial-gradient(circle,#3fa2ff 0%,#1d5fc0 25%,rgba(20,60,140,.5) 55%,rgba(10,26,68,0) 75%)}

/* client names */
.clients{left:0;top:620px;width:1200px;height:96px;background:#fff;display:flex;align-items:center;justify-content:space-between;padding:0 152px 0 154px;border-bottom:1px solid #eee}
.clients span{font-family:"Outfit",sans-serif;font-weight:500;font-size:24px;color:#3a3f48}

/* welcome */
.tile{border:9px solid var(--blue);padding:9px;background:#fff}
.tile.teal{border-color:var(--teal)}
.tile div{width:100%;height:100%}
.welcome-kicker{left:685px;top:784px;font-size:29px;font-weight:500;color:var(--ink)}
.welcome-name{left:684px;top:818px;font-size:56px;font-weight:500;color:var(--teal)}
.rule{height:2px;width:57px;background:var(--teal)}
.welcome-text{left:686px;top:930px;width:370px;font-size:17px;line-height:24.8px;color:#2a2e36;font-weight:300}
.welcome-btn{left:685px;top:1136px;width:150px;height:49px;font-size:16px;color:var(--white)}

/* services */
.services{left:0;top:1256px;width:1200px;height:1178px;background:radial-gradient(ellipse at 50% 40%,#1f6bbd 0%,var(--blue) 55%,#134f96 100%)}
.section-title{width:1200px;text-align:center;font-size:33px;font-weight:600}
.card{border:1px solid var(--blue-line);color:var(--white);padding:28px 36px}
.card.featured{background:var(--teal);border-color:var(--teal)}
.card svg{display:block;height:52px;margin-bottom:26px}
.card h3{font-family:"Exo 2",sans-serif;font-weight:600;font-size:13.5px;line-height:19px;text-transform:uppercase;margin-bottom:10px}
.card p{font-size:12.6px;line-height:18px;font-weight:300}
.wordmark{font-family:"Exo 2",sans-serif;font-size:30px;font-weight:500;height:52px;margin-bottom:26px;display:flex;align-items:center}

/* news */
.news{left:0;top:2434px;width:1200px;height:627px;background:linear-gradient(115deg,#f5f6f8 0%,#e7e9ed 45%,#f7f8fa 100%)}
.article{background:#fff;width:281px;height:401px}
.article.featured{background:var(--teal)}
.article .thumb{height:181px}
.article .body{padding:26px 27px}
.article h3{font-family:"Exo 2",sans-serif;font-size:13.5px;font-weight:600;text-transform:uppercase;margin-bottom:12px;color:var(--ink)}
.article p{font-size:12.6px;line-height:18px;color:#3a3f48;font-weight:300}
.article.featured h3,.article.featured p{color:#fff}
.read{display:inline-block;margin-top:16px;background:var(--teal);color:#fff;font-family:"Exo 2",sans-serif;font-size:11px;font-weight:600;padding:7px 10px;text-decoration:none}
.article.featured .read{background:#fff;color:var(--teal)}
.arrow{width:37px;height:37px;border:1.5px solid var(--teal);border-radius:50%;display:flex;align-items:center;justify-content:center}

/* subscribe */
.subscribe{left:0;top:3061px;width:1200px;height:417px;background:var(--sub-bg)}
.sub-art{left:57px;top:3104px;width:507px;height:364px;border-radius:50%;background:radial-gradient(circle at 55% 50%,#f3c48a 0%,#2f8da8 22%,rgba(22,88,110,.6) 50%,rgba(18,63,78,0) 72%)}
.sub-title{left:618px;top:3116px;color:#fff;font-weight:600;font-size:29px;line-height:41px}
.sub-title .accent{color:var(--teal);font-size:44px;line-height:52px}
.email{left:619px;top:3306px;width:434px;height:46px;background:#fff;display:flex;align-items:center;gap:14px;padding-left:18px;font-size:14px;color:#333}
.sub-btn{left:619px;top:3376px;width:170px;height:46px;font-size:17px;color:#fff}

/* footer */
.footer{left:0;top:3478px;width:1200px;height:199px;background:var(--navy-deep)}
.foot-nav{left:674px;top:3525px;display:flex;gap:30px}
.foot-nav a{color:#fff;font-family:"Exo 2",sans-serif;font-size:12.5px;font-weight:500;text-decoration:none}
.foot-rule{left:150px;top:3584px;width:900px;height:1px;background:#24345f}
.copy{left:0;top:3620px;width:1200px;text-align:center;color:#c9d0e0;font-size:11.5px}
</style>
</head>
<body>

<!-- header + hero -->
<section class="abs hero"></section>
<div class="abs hero-art" role="img" aria-label="Glowing blue AI microchip with circuit lines rising from it"></div>
<a class="abs brand" style="left:150px;top:28px"><span class="brand-square"></span>qorvanta</a>
<nav class="abs main-nav">
  <a class="active" href="#">HOME</a><a href="#">ABOUT</a><a href="#">SERVICES</a><a href="#">BLOG</a><a href="#">CONTACT</a>
</nav>
<div class="abs phone">
  <svg width="20" height="20" viewBox="0 0 24 24" fill="none" stroke="#fff" stroke-width="1.6"><path d="M5 3h4l2 5-2.5 1.5a11 11 0 0 0 6 6L16 13l5 2v4a2 2 0 0 1-2 2A16 16 0 0 1 3 5a2 2 0 0 1 2-2z"/></svg>
  1800 555 019
</div>
<h1 class="abs display hero-title"><span class="accent">Driving Innovation</span><br>with Advanced AI-Powered<br>Software Solutions</h1>
<p class="abs hero-sub">Empowering businesses with cutting-edge<br>AI technology for smarter, faster results</p>
<a class="abs btn hero-btn" href="#">Book Free Consultation</a>
<div class="abs dots"><span class="on"></span><span></span><span></span><span></span></div>

<!-- clients -->
<div class="abs clients"><span>Norvel</span><span>Kestrabyte</span><span>Trevalo</span><span>Brightwell</span></div>

<!-- welcome -->
<div class="abs tile" style="left:150px;top:789px;width:232px;height:131px"><div role="img" aria-label="Engineers working at laptops in a modern office" style="background:linear-gradient(135deg,#8b97a8,#3d4a5c)"></div></div>
<div class="abs tile teal" style="left:150px;top:940px;width:232px;height:246px"><div role="img" aria-label="Engineer with a laptop in a server room" style="background:linear-gradient(160deg,#1c2f55,#5f7fa8 60%,#1a2540)"></div></div>
<div class="abs tile" style="left:405px;top:788px;width:231px;height:232px"><div role="img" aria-label="Hands on a laptop with digital code overlay" style="background:linear-gradient(150deg,#0f3a4e,#1f7f8a 50%,#0b2030)"></div></div>
<div class="abs tile teal" style="left:405px;top:1037px;width:231px;height:152px"><div role="img" aria-label="Glowing cloud over a digital landscape" style="background:radial-gradient(circle at 50% 45%,#9fd0ff,#1c4fb0 45%,#0a1640)"></div></div>

<p class="abs display welcome-kicker">Welcome to</p>
<h2 class="abs display welcome-name">Qorvanta</h2>
<div class="abs rule" style="left:687px;top:897px"></div>
<p class="abs welcome-text">At Qorvanta, we craft bespoke software solutions that are not available on the market. By building organizations market-leading products, process automation, legacy system enablement, or advanced intelligent systems, we empower our customers to achieve a competitive edge in their industry.</p>
<a class="abs btn welcome-btn" href="#">Read More</a>

<!-- services -->
<section class="abs services"></section>
<h2 class="abs display section-title" style="left:0;top:1309px;color:#fff">Our Services</h2>
<div class="abs" style="left:573px;top:1378px;width:54px;height:2px;background:#fff"></div>

<article class="abs card featured" style="left:150px;top:1440px;width:281px;height:258px">
  <svg viewBox="0 0 52 52" width="52" fill="none" stroke="#fff" stroke-width="2"><rect x="6" y="12" width="40" height="26" rx="2"/><path d="M18 46h16M26 38v8"/><circle cx="26" cy="25" r="6"/><path d="M26 4v6M16 8l3 4M36 8l-3 4"/></svg>
  <h3>Enterprise Systems<br>Integration</h3>
  <p>Automate your business processes internally or externally to improve data quality and process efficiency</p>
</article>
<article class="abs card" style="left:459px;top:1440px;width:282px;height:258px">
  <svg viewBox="0 0 52 52" width="52" fill="none" stroke="#fff" stroke-width="2"><circle cx="26" cy="26" r="8"/><circle cx="26" cy="26" r="3"/><path d="M6 6h8M6 6v8M46 6h-8M46 6v8M6 46h8M6 46v-8M46 46h-8M46 46v-8"/></svg>
  <h3>Microservices</h3>
  <p>Leverage Microservices Architecture to enable quick deployment, dynamically scalable service performance, team productivity and more</p>
</article>
<article class="abs card" style="left:769px;top:1440px;width:281px;height:258px">
  <svg viewBox="0 0 52 52" width="52" fill="none" stroke="#fff" stroke-width="2"><path d="M14 34a9 9 0 0 1 1-18 12 12 0 0 1 23 2 8 8 0 0 1 0 16z"/><circle cx="26" cy="26" r="5"/><path d="M26 39v8M18 39l-4 7M34 39l4 7"/></svg>
  <h3>Platform Engineering</h3>
  <p>For organisations looking to manage the security and cost risks around their cloud infrastructure management for applications</p>
</article>

<article class="abs card" style="left:150px;top:1722px;width:281px;height:306px">
  <svg viewBox="0 0 52 52" width="52" fill="#fff"><path d="M20 12l4 12 12 4-12 4-4 12-4-12-12-4 12-4z"/><path d="M38 4l2 6 6 2-6 2-2 6-2-6-6-2 6-2z"/><path d="M38 34l1.5 4 4 1.5-4 1.5-1.5 4-1.5-4-4-1.5 4-1.5z"/></svg>
  <h3>Conversational AI</h3>
  <p>Enabling legacy systems with conversational user interfaces, or simply building intelligent natural language based services, conversational AI has many use cases across sales and operations.</p>
</article>
<article class="abs card" style="left:459px;top:1722px;width:282px;height:306px">
  <svg viewBox="0 0 52 52" width="52" fill="none" stroke="#fff" stroke-width="2"><path d="M8 46V26M18 46V18M28 46V22M38 46V12"/><path d="M6 18l12-8 10 6 14-10"/><circle cx="30" cy="40" r="6"/></svg>
  <h3>Real-Time Data Stream<br>Processing</h3>
  <p>Being able to react to changing business conditions in a precise intelligent way is becoming increasingly important. Knowing how to manage real-time data streams around your organisation is the key to unlocking this capability</p>
</article>
<article class="abs card" style="left:769px;top:1722px;width:281px;height:306px">
  <div class="wordmark">flowrail</div>
  <h3>Flowrail</h3>
  <p>Our expertise in platform engineering, iPaaS, building distributed systems and enterprise systems integration has converted into a product offering helping small to medium business solve their own complex systems integration problems</p>
</article>

<article class="abs card" style="left:150px;top:2052px;width:281px;height:305px">
  <svg viewBox="0 0 52 52" width="52" fill="none" stroke="#fff" stroke-width="2"><path d="M26 4l20 10v24L26 48 6 38V14z"/><path d="M14 20l12 6 12-6-12-6zM14 26l12 6 12-6M14 32l12 6 12-6"/></svg>
  <h3>Integration Platform as<br>a Service (iPaaS)</h3>
  <p>Enabling legacy systems with conversational user interfaces, or simply building intelligent natural language based services, conversational AI has many use cases across sales and operations.</p>
</article>
<article class="abs card" style="left:459px;top:2052px;width:282px;height:305px">
  <svg viewBox="0 0 52 52" width="52" fill="#fff"><circle cx="26" cy="16" r="10"/><path d="M8 48c0-12 8-18 18-18s18 6 18 18z"/></svg>
  <h3>A.I. Agents</h3>
  <p>The future of business AI are autonomous agents that specialise in your business data and processes. Not only doing the current work well, but enabling intelligence and insight along the way</p>
</article>
<article class="abs card" style="left:769px;top:2052px;width:281px;height:305px">
  <svg viewBox="0 0 52 52" width="52" fill="none" stroke="#fff" stroke-width="2"><path d="M14 46V36a16 16 0 1 1 22-6l4 6h-6v10"/><circle cx="25" cy="20" r="5"/></svg>
  <h3>Technology Expertise</h3>
  <p>Integration Platform as a Service brings the power of cloud based services to traditional systems integration. This is the new integration approach that enables quick, efficient and reliable enterprise systems integration</p>
</article>

<!-- news -->
<section class="abs news"></section>
<h2 class="abs display section-title" style="left:0;top:2489px;color:var(--ink)">News &amp; Articles</h2>
<div class="abs" style="left:573px;top:2558px;width:54px;height:2px;background:var(--blue)"></div>

<div class="abs arrow" style="left:63px;top:2776px"><svg width="12" height="12" viewBox="0 0 12 12" fill="none" stroke="#4fc3b8" stroke-width="1.6"><path d="M8 1L3 6l5 5"/></svg></div>
<div class="abs arrow" style="left:1099px;top:2776px"><svg width="12" height="12" viewBox="0 0 12 12" fill="none" stroke="#4fc3b8" stroke-width="1.6"><path d="M4 1l5 5-5 5"/></svg></div>

<article class="abs article featured" style="left:150px;top:2606px">
  <div class="thumb" role="img" aria-label="Engineer in front of wall of data screens" style="background:linear-gradient(135deg,#0c2440,#2f6fa6 55%,#0b1e36)"></div>
  <div class="body"><h3>AI in Software Engineering</h3>
  <p>(CodeHarbor Blog) CodeHarbor Pilot is widely known for its code generation feature. Learn how the AI assistant's abilities can extend beyond just code generation.</p>
  <a class="read" href="#">READ MORE</a></div>
</article>
<article class="abs article" style="left:461px;top:2606px">
  <div class="thumb" role="img" aria-label="Hands typing on laptop with chat interface overlay" style="background:linear-gradient(135deg,#7a4fa0,#c7b5dd 55%,#5a86c0)"></div>
  <div class="body"><h3>Conversational Interfaces</h3>
  <p>(Kestrabyte Learning) A chatbot is an application that has written or spoken natural language as its user interface. In other words, a conversation is the means through</p>
  <a class="read" href="#">READ MORE</a></div>
</article>
<article class="abs article" style="left:771px;top:2606px">
  <div class="thumb" role="img" aria-label="Businessman touching a holographic AI interface" style="background:linear-gradient(135deg,#0f2338,#3d6580 55%,#101c2b)"></div>
  <div class="body"><h3>Artificial Intelligence</h3>
  <p>(Kestrabyte Research) A surge of generative AI models in the past year has fueled much discussion about the impact of artificial intelligence on human history.</p>
  <a class="read" href="#">READ MORE</a></div>
</article>

<!-- subscribe -->
<section class="abs subscribe"></section>
<div class="abs sub-art" role="img" aria-label="Hand holding a glowing AI globe surrounded by technology icons over a world map"></div>
<h2 class="abs display sub-title"><span class="accent">Australia's</span><br>Largest Health Charity<br>Implements Qorvanta<br>API Msg Bus</h2>
<label class="abs email">
  <svg width="16" height="12" viewBox="0 0 16 12" fill="#1a2540"><path d="M0 0h16v12H0z"/><path d="M0 0l8 6 8-6" stroke="#fff" fill="none"/></svg>
  Email id
</label>
<a class="abs btn sub-btn" href="#">Subscribe</a>

<!-- footer -->
<footer class="abs footer"></footer>
<a class="abs brand" style="left:151px;top:3512px"><span class="brand-square"></span>qorvanta</a>
<nav class="abs foot-nav"><a href="#">HOME</a><a href="#">ABOUT</a><a href="#">SERVICES</a><a href="#">BLOG</a><a href="#">CONTACT</a></nav>
<div class="abs foot-rule"></div>
<p class="abs copy">Privacy Policy &nbsp; | &nbsp; © 2025 Ironkeel Networks. All rights reserved.</p>

</body>
</html>
```